Flyer-Design für Schädlingsbekämpfung
Zielgruppe
Schädlingsbekämpfung, Zielgruppe ab 30 Jahren.
Schwerpunkt Wespenbekämpfung.
Aufgabenstellung
Neben der Wespenbekämpfung sollten noch die allgemeine Schädlingsbekämpfung ihren Platz finden.

```html
<!DOCTYPE html>
<html lang="de">
<head>
<meta charset="utf-8">
<title>Flyer Schädlingsbekämpfung</title>
<link href="https://fonts.googleapis.com/css2?family=Roboto:wght@300;400;500;700&display=swap" rel="stylesheet">
<style>
:root{
  --green:#1e9a46;
  --green-dark:#15803a;
  --ink:#1d1d1b;
  --grey:#4a4a4a;
  --paper:#ffffff;
  --backdrop:#dcdcdc;
}
*{box-sizing:border-box;margin:0;padding:0}
html,body{width:1200px;height:800px;overflow:hidden}
body{background:var(--backdrop);font-family:'Roboto',Arial,sans-serif;color:var(--ink);position:relative}
.flyer{position:absolute;top:29px;width:350px;height:742px;background:var(--paper);overflow:hidden;box-shadow:0 2px 10px rgba(0,0,0,.12)}
.flyer--wasp{left:235px}
.flyer--services{left:615px}
.brand{position:absolute;top:22px;left:22px;right:20px;height:72px}
.brand__name{position:absolute;left:0;top:10px;color:var(--green);font-weight:500;font-size:19px;line-height:1.15;letter-spacing:.3px;text-transform:uppercase}
.brand__name small{display:block;font-size:12px;letter-spacing:.5px;text-transform:none}
.brand__dot{position:absolute;right:0;top:0;width:66px;height:66px;border-radius:50%;background:var(--green)}
.headline{font-weight:700;font-size:19px;line-height:1.2;color:var(--ink)}
/* wasp flyer */
.species-band{position:absolute;top:118px;left:0;width:190px;height:24px;background:var(--green);color:#fff;font-size:12px;font-weight:500;letter-spacing:.6px;padding:5px 0 0 22px}
.photo{position:absolute}
.photo--wasps{top:142px;left:0;width:190px;height:270px;background:linear-gradient(160deg,#6d7a3c 0%,#b58d52 35%,#d8b47a 60%,#8c6a3e 100%)}
.intro{position:absolute;top:108px;left:205px;width:132px}
.intro__text{margin-top:12px;font-size:11.2px;line-height:1.45;color:var(--grey);font-weight:300;text-align:justify;hyphens:manual}
.benefits{position:absolute;top:440px;left:24px;list-style:none}
.benefits li{display:flex;align-items:center;gap:12px;font-size:12.5px;font-weight:500;margin-bottom:12px}
.benefits svg{width:20px;height:16px;flex:none}
.feature-row{position:absolute;top:548px;left:0;width:100%;height:92px;display:flex;justify-content:space-between;padding:0 0}
.feature-tile{width:104px;height:92px;background:var(--green);display:flex;align-items:center;justify-content:center}
.feature-tile svg{width:46px;height:46px}
.contact-mail{position:absolute;left:0;width:100%;display:flex;align-items:center;justify-content:center;gap:10px;font-size:17px;font-weight:500}
.contact-mail svg{width:18px;height:14px}
.flyer--wasp .contact-mail{top:680px}
/* services flyer */
.services-head{position:absolute;top:116px;left:26px;width:290px}
.services{position:absolute;top:184px;left:26px;list-style:none}
.services li{display:flex;align-items:center;gap:12px;font-size:13.5px;font-weight:300;margin-bottom:9px;color:var(--grey)}
.services svg{width:15px;height:15px;flex:none}
.photo--tree{left:0;top:470px;width:112px;height:108px;background:linear-gradient(150deg,#4f6b36,#8aa35e 55%,#dfe6cf)}
.photo--treatment{left:118px;top:420px;width:112px;height:108px;background:linear-gradient(150deg,#e6dccf,#c9b8a3 50%,#f3efe9)}
.photo--technician{left:236px;top:370px;width:114px;height:108px;background:linear-gradient(150deg,#f1ece4,#b9bcc4 50%,#d8c4a6)}
.address{position:absolute;top:592px;left:26px;font-size:12px;line-height:1.35;color:var(--grey)}
.address strong{font-weight:500;color:var(--ink)}
.phone-band{position:absolute;top:644px;left:0;width:100%;height:58px;background:var(--green);padding:8px 0 0 40px}
.phone-band p{display:flex;align-items:center;gap:10px;font-size:17px;font-weight:500;color:var(--ink);line-height:1.3}
.phone-band svg{width:13px;height:13px}
.flyer--services .contact-mail{top:712px}
</style>
</head>
<body>

<article class="flyer flyer--wasp">
  <header class="brand">
    <p class="brand__name">Schädlingsfrei<br>Jonas Wendler<small>Bad Lindenau</small></p>
    <span class="brand__dot"></span>
  </header>

  <div class="species-band">FELDWESPE</div>
  <div class="photo photo--wasps" role="img" aria-label="Foto: Feldwespen auf ihrem Wabennest"></div>

  <section class="intro">
    <h1 class="headline">Sie benötigen schnelle Hilfe bei Problemen mit Wespen?</h1>
    <p class="intro__text">Die Deutsche und die Gemeine Wespe bauen sehr große Nester in Siedlungs&shy;nähe vor allem in dunklen Erhöhen, Verkleidungen, Roll&shy;ladenkästen, Dach&shy;räumen und Schup&shy;pen. Diese beiden Arten „fliegen“ auf Süßes und können dadurch lästig werden.</p>
  </section>

  <ul class="benefits">
    <li><svg viewBox="0 0 20 16"><path d="M2 7l6 7L18 2" fill="none" stroke="var(--green)" stroke-width="2.6" stroke-linecap="round" stroke-linejoin="round"/></svg>dauerhafte Entfernung / Umsiedlung</li>
    <li><svg viewBox="0 0 20 16"><path d="M2 7l6 7L18 2" fill="none" stroke="var(--green)" stroke-width="2.6" stroke-linecap="round" stroke-linejoin="round"/></svg>schnell, nachhaltig und einfach</li>
    <li><svg viewBox="0 0 20 16"><path d="M2 7l6 7L18 2" fill="none" stroke="var(--green)" stroke-width="2.6" stroke-linecap="round" stroke-linejoin="round"/></svg>fachgerechte Bekämpfung mit Erfahrung</li>
  </ul>

  <div class="feature-row">
    <div class="feature-tile">
      <svg viewBox="0 0 48 48"><circle cx="27" cy="27" r="15" fill="none" stroke="var(--ink)" stroke-width="4"/><path d="M27 27V18M27 12V7M22 6h10M4 22h8M2 29h8M5 36h8" stroke="var(--ink)" stroke-width="4" stroke-linecap="round"/></svg>
    </div>
    <div class="feature-tile">
      <svg viewBox="0 0 48 48"><rect x="14" y="16" width="18" height="28" rx="3" fill="var(--ink)"/><rect x="18" y="9" width="10" height="7" fill="var(--ink)"/><circle cx="33" cy="6" r="1.6" fill="var(--ink)"/><circle cx="37" cy="9" r="1.6" fill="var(--ink)"/><circle cx="37" cy="3" r="1.6" fill="var(--ink)"/><circle cx="23" cy="31" r="4" fill="var(--green)"/></svg>
    </div>
    <div class="feature-tile">
      <svg viewBox="0 0 48 48"><circle cx="24" cy="25" r="18" fill="none" stroke="var(--ink)" stroke-width="4"/><path d="M15 24l8 8L42 8" fill="none" stroke="var(--ink)" stroke-width="5" stroke-linecap="round" stroke-linejoin="round"/></svg>
    </div>
  </div>

  <p class="contact-mail"><svg viewBox="0 0 18 14"><rect width="18" height="14" fill="var(--ink)"/><path d="M0 0l9 7 9-7" fill="none" stroke="#fff" stroke-width="1.5"/></svg>lumbart@sjw-bl.de</p>
</article>

<article class="flyer flyer--services">
  <header class="brand">
    <p class="brand__name">Schädlingsfrei<br>Jonas Wendler<small>Bad Lindenau</small></p>
    <span class="brand__dot"></span>
  </header>

  <h2 class="headline services-head">Ihr Fachbetrieb in<br>Bad Lindenau für:</h2>

  <ul class="services">
    <li><svg viewBox="0 0 16 16"><circle cx="8" cy="8" r="8" fill="var(--green)"/><path d="M4.5 8.3l2.4 2.4 4.6-5" fill="none" stroke="#fff" stroke-width="1.8"/></svg>Holz- und Bautenschutz</li>
    <li><svg viewBox="0 0 16 16"><circle cx="8" cy="8" r="8" fill="var(--green)"/><path d="M4.5 8.3l2.4 2.4 4.6-5" fill="none" stroke="#fff" stroke-width="1.8"/></svg>Hausbockbekämpfung</li>
    <li><svg viewBox="0 0 16 16"><circle cx="8" cy="8" r="8" fill="var(--green)"/><path d="M4.5 8.3l2.4 2.4 4.6-5" fill="none" stroke="#fff" stroke-width="1.8"/></svg>Hausschwammbekämpfung</li>
    <li><svg viewBox="0 0 16 16"><circle cx="8" cy="8" r="8" fill="var(--green)"/><path d="M4.5 8.3l2.4 2.4 4.6-5" fill="none" stroke="#fff" stroke-width="1.8"/></svg>Pilz/ Schimmelpilzsanierung</li>
    <li><svg viewBox="0 0 16 16"><circle cx="8" cy="8" r="8" fill="var(--green)"/><path d="M4.5 8.3l2.4 2.4 4.6-5" fill="none" stroke="#fff" stroke-width="1.8"/></svg>Schädlingsbekämpfung</li>
    <li><svg viewBox="0 0 16 16"><circle cx="8" cy="8" r="8" fill="var(--green)"/><path d="M4.5 8.3l2.4 2.4 4.6-5" fill="none" stroke="#fff" stroke-width="1.8"/></svg>Taubenabwehr</li>
    <li><svg viewBox="0 0 16 16"><circle cx="8" cy="8" r="8" fill="var(--green)"/><path d="M4.5 8.3l2.4 2.4 4.6-5" fill="none" stroke="#fff" stroke-width="1.8"/></svg>HACCP Service</li>
  </ul>

  <div class="photo photo--tree" role="img" aria-label="Foto: Sprühbehandlung an einem Baum"></div>
  <div class="photo photo--treatment" role="img" aria-label="Foto: Schädlingsbekämpfer im Schutzanzug bei der Behandlung eines Raumes"></div>
  <div class="photo photo--technician" role="img" aria-label="Foto: Techniker im Schutzanzug mit Sprühgerät"></div>

  <address class="address"><strong>SJW Bad Lindenau</strong><br>Lindenweg 14-16<br>55123 Bad Lindenau</address>

  <div class="phone-band">
    <p><svg viewBox="0 0 14 14"><path d="M3 1l2.5 3-1.5 1.5c.8 1.8 2.2 3.2 4 4L9.5 8l3 2.5L11 13C5.5 12.5 1.5 8.5 1 3z" fill="var(--ink)"/></svg>0612 / 480 31 276</p>
    <p><svg viewBox="0 0 14 14"><rect x="3" y="0" width="8" height="14" rx="1.5" fill="var(--ink)"/><rect x="4.5" y="2" width="5" height="8" fill="var(--green)"/></svg>0157 / 318 42 905</p>
  </div>

  <p class="contact-mail"><svg viewBox="0 0 18 14"><rect width="18" height="14" fill="var(--ink)"/><path d="M0 0l9 7 9-7" fill="none" stroke="#fff" stroke-width="1.5"/></svg>lumbart@sjw-bl.de</p>
</article>

</body>
</html>
```